Webshop Template

For our Webstore in UK we need a complete Template,
shoppingcart is Magento, the Shop is focussed on Download software,

the name: Codemeadowmart.co.uk

Check out some other good stores, like lumenkai.de

for example the Page from 

www.vorn.co.uk or

www.lumenkai.de

www.netholm.de

www.klickwaren.de

The Logodesign which are in Consideration

http://www.plotharbor.com/design/1431392/logo-design-by-talvin7qe

http://www.plotharbor.com/design/1429944/logo-design-by-milanhaskel

http://www.plotharbor.com/design/1428794/logo-design-by-fenwick-artworks

http://www.plotharbor.com/design/1427556/logo-design-by-quillodesk

http://www.plotharbor.com/design/1426888/logo-design-by-tavinu

http://www.plotharbor.com/design/1426630/logo-design-by-amber-reef-studio-

Target Market(s)

B2C - Consumer Marcet

Industry/Entity Type

Shop

```html
<!DOCTYPE html>
<html lang="en">
<head>
<meta charset="utf-8">
<title>Codemeadowmart.co.uk – Webshop Template</title>
<link rel="stylesheet" href="https://fonts.googleapis.com/css2?family=Oswald:wght@400;500&family=Arimo:wght@400;700&display=swap">
<style>
:root{
  --ink:#2b2b2b;
  --text:#555;
  --muted:#777;
  --teal:#5bb6cc;
  --teal-dark:#4aa3b9;
  --red:#b3262b;
  --bar:#111;
  --footer:#050505;
  --line:#e2e2e2;
  --page:#f3f3f3;
  --white:#fff;
}
*{box-sizing:border-box;margin:0;padding:0}
html,body{width:1200px;height:2482px;overflow:hidden}
body{background:var(--page);font-family:"Arimo",Arial,sans-serif;color:var(--text);position:relative}
a{color:inherit;text-decoration:none}

.topbar{position:absolute;left:0;top:0;width:1200px;height:44px;background:var(--bar);color:#ddd;font-size:13px;display:flex;align-items:center;justify-content:space-between;padding:0 26px 0 62px}
.topbar ul{list-style:none;display:flex;gap:24px;align-items:center}
.topbar .caret::after{content:"";display:inline-block;margin-left:8px;border:4px solid transparent;border-top-color:#bbb;vertical-align:-2px}

.site-header{position:absolute;left:50px;top:86px;width:1100px;height:60px}
.logo{position:absolute;left:30px;top:10px;font-family:"Arimo",Arial,sans-serif;font-weight:700;font-size:36px;color:var(--teal);letter-spacing:1px}
.cart-button{position:absolute;right:0;top:4px;width:142px;height:50px;background:var(--teal);color:#fff;font-size:11px;display:flex;align-items:center;justify-content:center;gap:10px;border:1px solid var(--teal-dark)}

.main-nav{position:absolute;left:50px;top:188px;width:1100px;height:56px;background:var(--white);border:1px solid #e6e6e6;display:flex;align-items:center;padding-left:22px}
.main-nav a{font-family:"Oswald",sans-serif;font-size:16px;color:var(--ink);padding:0 26px 0 0;margin-right:26px;border-right:1px solid #ddd;line-height:20px}
.main-nav a.active{color:var(--teal)}
.main-nav .spacer{width:1px;height:20px;background:#ddd;margin-left:256px}

.hero{position:absolute;left:50px;top:278px;width:1100px;height:494px;background:var(--white);border:1px solid #e4e4e4;overflow:hidden}
.hero h1{position:absolute;left:30px;top:16px;font-family:"Oswald",sans-serif;font-weight:500;font-size:58px;color:#333;letter-spacing:.5px}
.hero h1 span{color:var(--red)}
.hero p{position:absolute;left:32px;top:102px;width:660px;font-size:15px;line-height:22px;color:#333}
.hero-controls{position:absolute;right:10px;top:22px;width:202px;height:66px;background:#8e2a2a}
.hero-floor{position:absolute;left:0;top:360px;width:1100px;height:80px;background:linear-gradient(#f1f1f1,#fff)}
.hero-product{position:absolute;border-radius:4px}
.hero-label{position:absolute;top:432px;font-family:"Arimo",Arial,sans-serif;font-weight:700;font-size:19px;color:var(--red);letter-spacing:.5px;text-align:center}

.welcome{position:absolute;left:50px;top:806px;width:1100px}
.welcome h2{font-family:"Oswald",sans-serif;font-weight:400;font-size:48px;color:var(--ink);letter-spacing:.5px}
.welcome p{margin-top:12px;font-size:13px;line-height:21px;color:#444}

.product-block{position:absolute;left:50px;width:1100px}
.product-block .rule{height:4px;background:#e4e4e4}
.block-head{position:relative;height:70px}
.block-head h3{position:absolute;left:0;top:16px;font-family:"Oswald",sans-serif;font-weight:400;font-size:22px;color:var(--ink)}
.block-head::after{content:"";position:absolute;left:0;right:0;bottom:0;height:1px;background:var(--line)}
.block-head .short{position:absolute;left:0;bottom:0;width:26px;height:2px;background:#333;z-index:1}
.dots{position:absolute;right:0;top:28px;display:flex;gap:10px}
.dots i{width:11px;height:11px;border-radius:50%;background:#ddd;border:1px solid #ccc}
.dots i.on{background:var(--teal);border-color:var(--teal)}
.product-row{display:flex;justify-content:space-between;margin-top:24px}
.product-card{width:258px;height:376px;background:var(--white);border:1px solid #e6e6e6;padding:14px 14px 0;position:relative}
.product-image{width:228px;height:228px;border:1px solid #d8d8d8;display:flex;align-items:center;justify-content:center}
.product-image .art{width:130px;height:130px;border-radius:50%}
.product-card h4{margin-top:20px;font-family:"Oswald",sans-serif;font-weight:400;font-size:15px;color:var(--ink)}
.product-card p{margin-top:10px;font-size:14px;line-height:20px;color:var(--muted)}
.price{position:absolute;left:14px;bottom:18px;display:flex;align-items:center;font-family:"Oswald",sans-serif;font-size:16px;color:var(--ink)}
.price .divider{width:1px;height:18px;background:#ccc;margin:0 14px}

.pager{position:absolute;left:50px;top:2056px;width:1100px}
.pager .rule{height:4px;background:#e4e4e4}
.pager .buttons{position:absolute;right:0;top:22px;display:flex;gap:6px}
.pager .btn{width:34px;height:34px;display:flex;align-items:center;justify-content:center}
.pager .btn.prev{background:#e8e8e8;border:1px solid #d5d5d5}
.pager .btn.next{background:#000}

.site-footer{position:absolute;left:0;top:2128px;width:1200px;height:354px;background:var(--footer);color:#ccc}
.footer-col{position:absolute;top:46px;width:250px}
.footer-col h5{font-family:"Oswald",sans-serif;font-weight:400;font-size:16px;color:#fff;letter-spacing:.5px}
.footer-col .short{width:26px;height:1px;background:#666;margin:20px 0 24px}
.footer-col ul{list-style:none}
.links li{font-size:14px;color:var(--teal);margin-bottom:20px}
.social li{display:flex;align-items:center;gap:14px;font-size:14px;color:var(--teal);margin-bottom:14px}
.social .dot{width:20px;height:20px;border-radius:50%;background:#333}
.contact p{font-size:13px;line-height:20px;color:#ccc;margin-bottom:12px}
.contact b{color:#fff;font-weight:700}
.newsletter p{font-size:14px;line-height:22px;color:#ccc}
.newsletter form{display:flex;margin-top:14px}
.newsletter .field{width:222px;height:32px;background:#fff;border:0}
.newsletter .go{width:32px;height:32px;background:#fff;border-left:1px solid #ccc;display:flex;align-items:center;justify-content:center}
.footer-rule{position:absolute;left:50px;top:328px;width:1100px;height:1px;background:#222}
</style>
</head>
<body>

<header class="topbar">
  <ul>
    <li class="caret">Eng</li>
    <li class="caret">Usd</li>
    <li>Contact</li>
    <li>Site map</li>
    <li>Bookmark</li>
  </ul>
  <ul>
    <li>Your Account</li>
    <li>Login</li>
    <li><svg width="16" height="16" viewBox="0 0 16 16"><circle cx="6.5" cy="6.5" r="4.5" fill="none" stroke="#fff" stroke-width="2"/><line x1="10" y1="10" x2="14.5" y2="14.5" stroke="#fff" stroke-width="2.4"/></svg></li>
  </ul>
</header>

<div class="site-header">
  <div class="logo">LOGO</div>
  <a class="cart-button" href="#">
    <svg width="16" height="14" viewBox="0 0 16 14"><path d="M1 5h14l-2 8H3z" fill="#fff"/><path d="M5 5l3-4 3 4" fill="none" stroke="#fff" stroke-width="1.5"/></svg>
    0 PRODUCT
  </a>
</div>

<nav class="main-nav">
  <a class="active" href="#">HOME</a>
  <a href="#">PRODUCTS</a>
  <a href="#" style="border-right:0">ABOUT US</a>
  <span class="spacer"></span>
</nav>

<section class="hero">
  <h1><span>Updates</span> &amp; Downloads</h1>
  <p>Important new hardware updates are now available to optimize your Norvane PC's performance. Select your Norvane PC below to download now and enhance your computing experience.</p>
  <div class="hero-controls">
    <svg width="202" height="66" viewBox="0 0 202 66">
      <polygon points="14,33 30,20 30,28 46,28 46,38 30,38 30,46" fill="#d9a9a9"/>
      <rect x="86" y="16" width="10" height="34" fill="#d9a9a9"/>
      <rect x="104" y="16" width="10" height="34" fill="#d9a9a9"/>
      <polygon points="188,33 172,20 172,28 156,28 156,38 172,38 172,46" fill="#d9a9a9"/>
    </svg>
  </div>
  <div class="hero-floor"></div>
  <div class="hero-product" role="img" aria-label="Thin and light laptop" style="left:34px;top:288px;width:176px;height:130px;background:linear-gradient(#222,#555 80%,#bbb)"></div>
  <div class="hero-product" role="img" aria-label="Notebook computer" style="left:160px;top:278px;width:1px;height:1px"></div>
  <div class="hero-product" role="img" aria-label="Notebook computer" style="left:280px;top:276px;width:200px;height:150px;background:linear-gradient(#111,#444 78%,#999)"></div>
  <div class="hero-product" role="img" aria-label="All-in-one desktop PC" style="left:592px;top:168px;width:300px;height:256px;background:linear-gradient(#050505,#2a2a2a 78%,#aaa)"></div>
  <div class="hero-product" role="img" aria-label="Keyboard and trackpad accessories" style="left:930px;top:254px;width:108px;height:170px;background:linear-gradient(#e2e2e2,#b9b9b9)"></div>
  <div class="hero-label" style="left:28px;width:190px">THIN+LIGHT</div>
  <div class="hero-label" style="left:280px;width:200px">NOTEBOOK</div>
  <div class="hero-label" style="left:600px;width:290px">ALL-IN-ONE PC</div>
  <div class="hero-label" style="left:900px;width:200px">ACCESSORIES</div>
</section>

<section class="welcome">
  <h2>WELCOME</h2>
  <p>Parturient mollis ultricies fuga. Maiores elit nulla donec. Lorem cursus facilisi curabitur. Vel vel ut ut eu sed non sem. Ut duis tincidunt sagittis. Dolor consectetur ut nec. Unde mauris mauris suspendisse. Ut feugiat ante tellus eros eros vel justo felis viverra nunc vehicula. Porttitor at dis cras. Sagittis a massa vivamus. Erat odio mi magnis. Dignissim penatibus vel mattis. Erat rutrum in aliquam lectus non massa erat. Inceptos curabitur interdum magna. Ut arcu lacus odio vulputate ultricies placerat turpis. Urna tempor nec sodales. Penatibus sed orci viverra elit sit interdum magna ac posuere tortor vel. Elit facilisis ante sociosqu.</p>
</section>

<section class="product-block" style="top:1014px">
  <div class="rule"></div>
  <div class="block-head">
    <h3>Featured</h3><span class="short"></span>
    <div class="dots"><i></i><i></i><i></i><i class="on"></i><i></i></div>
  </div>
  <div class="product-row">
    <article class="product-card">
      <div class="product-image"><div class="art" role="img" aria-label="Browser software icon" style="background:radial-gradient(circle at 40% 40%,#f4a23a,#c2410c)"></div></div>
      <h4>DOLOR DONEC SAGITTIS</h4>
      <p>Quam duis ligula viverra. Vitae turpis elementum donec</p>
      <div class="price"><svg width="16" height="14" viewBox="0 0 16 14"><path d="M1 5h14l-2 8H3z" fill="var(--teal)"/><path d="M5 5l3-4 3 4" fill="none" stroke="var(--teal)" stroke-width="1.5"/></svg><span class="divider"></span>$139,00</div>
    </article>
    <article class="product-card">
      <div class="product-image"><div class="art" role="img" aria-label="Web browser software icon" style="background:radial-gradient(circle at 45% 45%,#7cc6f0,#1f6fb8)"></div></div>
      <h4>ANTE APTENT FEUGIAT</h4>
      <p>Eget vitae est sed. Nunc ex dui purus</p>
      <div class="price"><svg width="16" height="14" viewBox="0 0 16 14"><path d="M1 5h14l-2 8H3z" fill="var(--teal)"/><path d="M5 5l3-4 3 4" fill="none" stroke="var(--teal)" stroke-width="1.5"/></svg><span class="divider"></span>$139,00</div>
    </article>
    <article class="product-card">
      <div class="product-image"><div class="art" role="img" aria-label="Security software icon" style="border-radius:6px;background:linear-gradient(135deg,#e33,#9a1010 60%,#888)"></div></div>
      <h4>QUAM DUIS LIGULA</h4>
      <p>Libero sodales ante tincidunt in gravida volutpat</p>
      <div class="price"><svg width="16" height="14" viewBox="0 0 16 14"><path d="M1 5h14l-2 8H3z" fill="var(--teal)"/><path d="M5 5l3-4 3 4" fill="none" stroke="var(--teal)" stroke-width="1.5"/></svg><span class="divider"></span>$139,00</div>
    </article>
    <article class="product-card">
      <div class="product-image"><div class="art" role="img" aria-label="Voice call software icon" style="background:radial-gradient(circle at 45% 40%,#6fd0f5,#1377b0 70%,#555)"></div></div>
      <h4>VITAE TURPIS ELEMENTUM</h4>
      <p>Duis interdum sed est et nullam eu accumsan nam gravida</p>
      <div class="price"><svg width="16" height="14" viewBox="0 0 16 14"><path d="M1 5h14l-2 8H3z" fill="var(--teal)"/><path d="M5 5l3-4 3 4" fill="none" stroke="var(--teal)" stroke-width="1.5"/></svg><span class="divider"></span>$139,00</div>
    </article>
  </div>
</section>

<section class="product-block" style="top:1538px">
  <div class="rule"></div>
  <div class="block-head">
    <h3>New</h3><span class="short"></span>
    <div class="dots"><i></i><i></i><i></i><i class="on"></i><i></i></div>
  </div>
  <div class="product-row">
    <article class="product-card">
      <div class="product-image"><div class="art" role="img" aria-label="Media player software icon" style="border-radius:10px;background:linear-gradient(135deg,#bbb,#444 55%,#f29a1a)"></div></div>
      <h4>DOLOR DONEC SAGITTIS</h4>
      <p>Quam duis ligula viverra. Vitae turpis elementum donec</p>
      <div class="price"><svg width="16" height="14" viewBox="0 0 16 14"><path d="M1 5h14l-2 8H3z" fill="var(--teal)"/><path d="M5 5l3-4 3 4" fill="none" stroke="var(--teal)" stroke-width="1.5"/></svg><span class="divider"></span>$139,00</div>
    </article>
    <article class="product-card">
      <div class="product-image"><div class="art" role="img" aria-label="Disc burning software icon" style="background:radial-gradient(circle at 50% 45%,#e8542a,#777 60%,#ccc)"></div></div>
      <h4>ANTE APTENT FEUGIAT</h4>
      <p>Eget vitae est sed. Nunc ex dui purus</p>
      <div class="price"><svg width="16" height="14" viewBox="0 0 16 14"><path d="M1 5h14l-2 8H3z" fill="var(--teal)"/><path d="M5 5l3-4 3 4" fill="none" stroke="var(--teal)" stroke-width="1.5"/></svg><span class="divider"></span>$139,00</div>
    </article>
    <article class="product-card">
      <div class="product-image"><div class="art" role="img" aria-label="File sharing software icon" style="border-radius:30%;background:linear-gradient(#9b8466,#3a9a2e)"></div></div>
      <h4>QUAM DUIS LIGULA</h4>
      <p>Libero sodales ante tincidunt in gravida volutpat</p>
      <div class="price"><svg width="16" height="14" viewBox="0 0 16 14"><path d="M1 5h14l-2 8H3z" fill="var(--teal)"/><path d="M5 5l3-4 3 4" fill="none" stroke="var(--teal)" stroke-width="1.5"/></svg><span class="divider"></span>$139,00</div>
    </article>
    <article class="product-card">
      <div class="product-image"><div class="art" role="img" aria-label="Music library software icon" style="background:radial-gradient(circle at 45% 45%,#4fc3e8,#2a3a8a 60%,#888)"></div></div>
      <h4>VITAE TURPIS ELEMENTUM</h4>
      <p>Duis interdum sed est et nullam eu accumsan nam gravida</p>
      <div class="price"><svg width="16" height="14" viewBox="0 0 16 14"><path d="M1 5h14l-2 8H3z" fill="var(--teal)"/><path d="M5 5l3-4 3 4" fill="none" stroke="var(--teal)" stroke-width="1.5"/></svg><span class="divider"></span>$139,00</div>
    </article>
  </div>
</section>

<div class="pager">
  <div class="rule"></div>
  <div class="buttons">
    <span class="btn prev"><svg width="8" height="10" viewBox="0 0 8 10"><polygon points="6,1 2,5 6,9" fill="#666"/></svg></span>
    <span class="btn next"><svg width="8" height="10" viewBox="0 0 8 10"><polygon points="2,1 6,5 2,9" fill="#fff"/></svg></span>
  </div>
</div>

<footer class="site-footer">
  <div class="footer-col" style="left:50px">
    <h5>INFORMATION</h5><div class="short"></div>
    <ul class="links">
      <li>Specials</li><li>New products</li><li>Top sellers</li><li>Contact us</li><li>Terms and conditions of use</li>
    </ul>
  </div>
  <div class="footer-col" style="left:330px">
    <h5>FOLLOW US</h5><div class="short"></div>
    <ul class="social">
      <li><span class="dot"></span>Friendwall</li>
      <li><span class="dot"></span>Chirpline</li>
      <li><span class="dot"></span>RSS</li>
      <li><span class="dot"></span>Orbitplus</li>
    </ul>
  </div>
  <div class="footer-col contact" style="left:612px">
    <h5>CONTACT US</h5><div class="short"></div>
    <p>Etiam justo lectus, placerat vel aliquet &nbsp;varius quis mauris.</p>
    <p><b>Add.</b> 9604 Nulla vitae elit liberophare tra augue.</p>
    <p><b>Mobile.</b> +123 456 7890</p>
    <p><b>Email.</b></p>
  </div>
  <div class="footer-col newsletter" style="left:894px">
    <h5>NEWSLETTER</h5><div class="short"></div>
    <p>Subscribe our newsletter to receive our newest promo</p>
    <form>
      <span class="field"></span>
      <span class="go"><svg width="12" height="10" viewBox="0 0 12 10"><path d="M1 5h9M7 2l3 3-3 3" fill="none" stroke="#333" stroke-width="1.4"/></svg></span>
    </form>
  </div>
  <div class="footer-rule"></div>
</footer>

</body>
</html>
```